Non-fiction book about abuse and survival, needs cover design

This book is about me, and a lifetime of abuse that I survived. The goal is to help others in abusive situations break the cycle of shame that accompanies unhealthy and toxic relationships. I want the cover to illustrate a vast and sometimes scary world where we victims feel alone. It's up to us to choose our destiny, and sometimes we must do that when others don't agree. But there is hope. No longer do we need to believe the lie that something broken is better than nothing at all. After reading this, others will learn to trust their intuition, and how to avoid the pitfalls and red flags of toxic relationships. I want the cover to also show strength, hope, and positivity in the face of adversity. The picture of me (attached) is a good start to show a great big and sometimes frightening world a victim of abuse lives in. I love nature photos, but it's not a requirement for this project. I prefer simple designs. Thank you so much!

Target Market(s)

Survivors of abuse, at risk youth, and friends/family with loved ones who are abused

Requirements
Must have
• Title: The Lantern Keeper
Subtitle: Leave the Crooked Road That Runs Past Every Open Gate You Were Shown
Nice to have
• Outdoor scenery, open spaces.

```html
<!DOCTYPE html>
<html lang="en">
<head>
<meta charset="utf-8">
<title>The Lantern Keeper — Cover Wrap</title>
<link rel="stylesheet" href="https://fonts.googleapis.com/css2?family=Bebas+Neue&family=Oswald:wght@300;600&family=Libre+Baskerville&display=swap">
<style>
  :root {
    --page-bg: #efefef;
    --paper: #ffffff;
    --ink: #1c1c1c;
    --title: #fbfaf6;
    --violet: #8a5ad8;
    --magenta: #d2437a;
    --crimson: #c8322e;
    --ochre: #c88a4e;
    --sand: #b98a62;
    --rust: #9a3a2c;
  }
  * { box-sizing: border-box; margin: 0; padding: 0; }
  html, body { width: 899px; height: 1200px; overflow: hidden; background: var(--page-bg); }
  .wrap {
    position: absolute; left: 20px; top: 301px;
    width: 860px; height: 597px;
    display: flex;
  }
  .panel { position: relative; height: 100%; overflow: hidden; }
  .back { width: 396px; }
  .spine { width: 67px; background: var(--paper); }
  .front { width: 397px; }
  .scenery { position: absolute; inset: 0; }
  .back .scenery {
    background:
      radial-gradient(ellipse at 30% 20%, var(--magenta) 0%, transparent 55%),
      radial-gradient(ellipse at 80% 85%, var(--ochre) 0%, transparent 55%),
      linear-gradient(160deg, var(--crimson) 0%, var(--magenta) 40%, var(--sand) 75%, var(--rust) 100%);
  }
  .front .scenery {
    background:
      radial-gradient(ellipse at 40% 78%, #e9ddd2 0%, transparent 22%),
      radial-gradient(ellipse at 85% 20%, var(--crimson) 0%, transparent 45%),
      linear-gradient(180deg, var(--violet) 0%, var(--magenta) 18%, var(--ochre) 45%, var(--sand) 70%, var(--rust) 100%);
  }
  .title {
    position: absolute; left: 24px;
    font-family: "Bebas Neue", sans-serif;
    font-weight: 400;
    color: var(--title);
    line-height: 0.9;
    white-space: nowrap;
    text-shadow: 2px 3px 4px rgba(0,0,0,0.35);
  }
  .title .lead { display: block; font-size: 72px; }
  .title .main { display: block; font-size: 128px; letter-spacing: 1px; }
  .back .title { top: 28px; left: 32px; }
  .front .title { top: 28px; }
  .subtitle-band {
    position: absolute; top: 224px; right: 0; width: 300px; height: 92px;
    background: var(--paper);
    padding: 8px 14px 0 8px;
    text-align: right;
    font-family: "Oswald", sans-serif; font-weight: 300;
    font-size: 16px; line-height: 25px; text-transform: uppercase;
    color: var(--ink);
  }
  .subtitle-band span { display: block; white-space: nowrap; }
  .author {
    position: absolute; left: 0; right: 0; bottom: 34px;
    text-align: center;
    white-space: nowrap;
    font-family: "Oswald", sans-serif; font-weight: 600;
    font-size: 19px; letter-spacing: 8px;
    color: var(--title);
    text-shadow: 1px 2px 3px rgba(0,0,0,0.4);
  }
  .blurb {
    position: absolute; left: 34px; top: 140px;
    width: 325px; height: 325px; border-radius: 50%;
    background: var(--paper);
    display: flex; flex-direction: column; justify-content: center; align-items: center;
    font-family: "Libre Baskerville", serif;
    font-size: 10.4px; line-height: 13.2px; color: var(--ink);
    text-align: center;
  }
  .blurb span { display: block; white-space: nowrap; }
  .spine-text {
    position: absolute; left: 50%; top: 50%;
    transform: translate(-50%, -50%) rotate(-90deg);
    white-space: nowrap;
    display: flex; align-items: center; gap: 40px;
    color: var(--ink);
  }
  .spine-title { font-family: "Oswald", sans-serif; font-weight: 600; font-size: 21px; letter-spacing: 9px; }
  .spine-author { font-family: "Oswald", sans-serif; font-weight: 600; font-size: 10px; letter-spacing: 3px; }
</style>
</head>
<body>
  <div class="wrap">
    <section class="panel back">
      <div class="scenery" role="img" aria-label="Painted desert canyon in crimson, magenta and ochre tones"></div>
      <h2 class="title"><span class="lead">THE LANTERN</span><span class="main">KEEPER</span></h2>
      <div class="blurb">
        <span>Lorem ipsum dolor sit</span>
        <span>amet, consectetur adipiscing elit.</span>
        <span>Quisque non odio vitae metus iaculis</span>
        <span>aliquet in sed erat. Donec id lectus risus.</span>
        <span>Proin non orci gravida, interdum odio non, dapi-</span>
        <span>bus justo. Suspendisse aliquet lacus volutpat tortor</span>
        <span>volutpat hendrerit. Etiam quis pharetra metus. Mae-</span>
        <span>cenas finibus viverra mauris, at lacinia mi malesuada</span>
        <span>in. Donec finibus, mauris non suscipit aliquet, neque ante</span>
        <span>consequat nulla, et sodales orci neque vel mauris. Donec</span>
        <span>auctor arcu quis malesuada euismod. Suspendisse sit</span>
        <span>amet tempor leo, a tempus metus. Quisque porta semper</span>
        <span>placerat. Proin nec condimentum sem. Cras dictum</span>
        <span>pulvinar enim sed rutrum. Suspendisse commodo</span>
        <span>sapien nec lacus accumsan semper. Nulla commo-</span>
        <span>do, nisl eget pulvinar imperdiet, tellus tellus ul-</span>
        <span>trices dui, ut imperdiet risus lorem ac ipsum.</span>
      </div>
    </section>
    <section class="panel spine">
      <div class="spine-text">
        <span class="spine-author">MARISOL KETTERING</span>
        <span class="spine-title">THE LANTERN KEEPER</span>
      </div>
    </section>
    <section class="panel front">
      <div class="scenery" role="img" aria-label="Painted desert landscape with red rock formations and a woman seen from behind, seated and looking out over the valley"></div>
      <h1 class="title"><span class="lead">THE LANTERN</span><span class="main">KEEPER</span></h1>
      <p class="subtitle-band"><span>Leave the crooked road that runs</span><span>past every open gate</span><span>you were shown</span></p>
      <p class="author">MARISOL KETTERING</p>
    </section>
  </div>
</body>
</html>
```